New signage for apartment community in the Pacific Northwest

Signage for an apartment community in the Pacific Northwest. It should have a contemporary northwest vibe with a fresh exciting feeling. We are open to the colors cayenne, white, charcoal and a splash of lime green. Sign to have the name 'VELTO' with the address number 28391 smaller underneath. sign can include a shape under the name or a feeling of energy in the shape of the name.

Target Market(s)

Young urban professionals

Industry/Entity Type

Real Estate Development

Requirements
Must have
• eyecatching
Should not have
• anything too cute or too busy

```html
<!DOCTYPE html>
<html lang="en">
<head>
<meta charset="utf-8">
<title>VELTO Apartments – Sign</title>
<link rel="stylesheet" href="https://fonts.googleapis.com/css2?family=Montserrat:ital,wght@0,800;1,800;1,900&display=swap">
<style>
  :root {
    --cayenne: #df4a53;
    --charcoal: #5a5a5a;
    --edge-grey: #878787;
    --white: #ffffff;
    --frame: #111111;
  }
  html, body {
    margin: 0;
    padding: 0;
    width: 1200px;
    height: 1200px;
    overflow: hidden;
    background: var(--white);
  }
  .canvas {
    width: 1200px;
    height: 1200px;
    display: block;
  }
  .sign-panel { fill: var(--white); stroke: var(--frame); stroke-width: 2; }
  .cayenne-field { fill: var(--cayenne); }
  .diagonal-edge { stroke: var(--edge-grey); stroke-width: 5; }
  .sign-name {
    font-family: "Montserrat", sans-serif;
    font-weight: 800;
    font-style: normal;
    font-size: 270px;
    fill: var(--charcoal);
  }
  .sign-type {
    font-family: "Montserrat", sans-serif;
    font-weight: 900;
    font-style: italic;
    font-size: 48px;
    fill: var(--charcoal);
  }
  .sign-address {
    font-family: "Montserrat", sans-serif;
    font-weight: 800;
    font-style: italic;
    font-size: 29px;
    fill: var(--charcoal);
  }
</style>
</head>
<body>
  <svg class="canvas" viewBox="0 0 1200 1200" xmlns="http://www.w3.org/2000/svg" role="img" aria-label="VELTO Apartments sign">
    <rect class="sign-panel" x="88" y="258" width="1043" height="694"/>
    <polygon class="cayenne-field" points="89,259 1124,259 89,942"/>
    <line class="diagonal-edge" x1="1130" y1="260" x2="89" y2="948"/>

    <text class="sign-name" x="152" y="705" textLength="886" lengthAdjust="spacingAndGlyphs">VELTO</text>

    <text class="sign-type" x="374" y="839" textLength="338" lengthAdjust="spacingAndGlyphs">APARTMENTS</text>
    <text class="sign-address" x="369" y="875" textLength="597" lengthAdjust="spacingAndGlyphs">28391 Alder Crest Way NE, Marlow, WA 98177</text>
  </svg>
</body>
</html>
```